Gourmet food made with love and care in my country kitchen

I'd like a business card designed for my small home-based food business. I have made labelling in federation blue for my food products (Labneh cheese, spicy pumpkin chutney, dukkah, caramelised onion jam, yo-Yo biscuits, chocolate mud cake etc) and have navy and white checked surrounds/borders on my brochures so would like to stick to these country colours.
Target Market(s)
Foodies who love gourmet delicacies. Everyone who enjoys a picnic that they don't have to prepare themselves.
Industry/Entity Type
Business
Contact Information for Business Card
Larkhollow Pantry
42 Tindale's Lane
Brimsworth Qld 4829
Phone Viv 07 48216597 or 0412386951
- Harrington

```html
<!DOCTYPE html>
<html lang="en">
<head>
<meta charset="utf-8">
<title>Larkhollow Pantry – Business Cards</title>
<link rel="stylesheet" href="https://fonts.googleapis.com/css2?family=Federant&family=Arimo:ital@1&family=Questrial&display=swap">
<style>
  :root {
    --navy: #1d2d6b;
    --arc-blue: #0f3f92;
    --arc-light: #5f8fd0;
    --card-edge: #b7cbe9;
    --card-mid: #e4ecf8;
    --card-centre: #ffffff;
    --bullet-red: #d2343b;
    --icon-navy: #1d2d6b;
    --text-grey: #2c2f3a;
    --label-grey: #2b2b2b;
    --frame: #d9d9d9;
  }
  html, body {
    margin: 0;
    padding: 0;
    width: 1200px;
    height: 2226px;
    overflow: hidden;
    background: #ffffff;
  }
  .sheet {
    position: relative;
    width: 1198px;
    height: 2224px;
    border: 1px solid var(--frame);
  }
  .variant-label {
    position: absolute;
    font-family: "Questrial", Arial, sans-serif;
    font-size: 38px;
    color: var(--label-grey);
    margin: 0;
    font-weight: normal;
  }
  .card {
    position: absolute;
    background: radial-gradient(ellipse 70% 75% at 55% 52%, var(--card-centre) 0%, var(--card-mid) 50%, var(--card-edge) 100%);
    box-shadow: 7px 9px 12px rgba(0, 0, 0, 0.32);
    overflow: hidden;
  }
  .card-art {
    position: absolute;
    left: 0;
    top: 0;
  }
  .brand-name {
    position: absolute;
    margin: 0;
    font-family: "Federant", Georgia, serif;
    font-weight: normal;
    color: var(--navy);
    white-space: nowrap;
    line-height: 1;
  }
  .services {
    position: absolute;
    margin: 0;
    padding: 0;
    list-style: none;
    font-family: "Federant", Georgia, serif;
    color: var(--text-grey);
  }
  .services li {
    position: relative;
    white-space: nowrap;
  }
  .services li::before {
    content: "";
    position: absolute;
    border-radius: 50%;
    background: var(--bullet-red);
    box-shadow: inset 0 0 0 3px var(--bullet-red), inset 0 0 0 6px #f3b9bb;
  }
  .tagline {
    position: absolute;
    margin: 0;
    font-family: "Arimo", Arial, sans-serif;
    font-style: italic;
    color: var(--navy);
  }
  .contacts {
    position: absolute;
    margin: 0;
    padding: 0;
    list-style: none;
    font-family: "Questrial", Arial, sans-serif;
    color: var(--text-grey);
  }
  .contacts li {
    display: flex;
    align-items: center;
    white-space: nowrap;
  }
  .contacts svg { flex: none; }

  /* single-sided card */
  .card--single { left: 108px; top: 131px; width: 972px; height: 597px; }
  .card--single .brand-name { left: 375px; top: 38px; font-size: 59px; }
  .card--single .services { left: 409px; top: 131px; font-size: 31px; line-height: 40px; }
  .card--single .services li::before { left: -27px; top: 13px; width: 14px; height: 14px; }
  .card--single .tagline { left: 249px; top: 303px; width: 440px; font-size: 21px; line-height: 26px; }
  .card--single .contacts { left: 72px; top: 398px; font-size: 23px; line-height: 34px; }
  .card--single .contacts svg { width: 26px; height: 26px; margin-right: 18px; }

  /* double-sided: front */
  .card--front { left: 111px; top: 908px; width: 935px; height: 556px; }
  .card--front .brand-name { left: 71px; top: 80px; font-size: 63px; }
  .card--front .services { left: 99px; top: 204px; font-size: 35px; line-height: 45px; }
  .card--front .services li::before { left: -27px; top: 15px; width: 15px; height: 15px; }
  .card--front .tagline { left: 75px; top: 378px; width: 560px; font-size: 25px; line-height: 31px; }

  /* double-sided: back */
  .card--back { left: 111px; top: 1543px; width: 941px; height: 557px; }
  .card--back .brand-name { left: 350px; top: 58px; font-size: 63px; }
  .card--back .contacts { left: 362px; top: 218px; font-size: 24px; line-height: 48px; }
  .card--back .contacts svg { width: 26px; height: 26px; margin-right: 16px; }
  .card--back .contacts .icon { fill: var(--bullet-red); stroke: var(--bullet-red); }
</style>
</head>
<body>
<svg width="0" height="0" style="position:absolute" aria-hidden="true">
  <defs>
    <linearGradient id="countryside" x1="0" y1="0" x2="0" y2="1">
      <stop offset="0" stop-color="#cfe0ee"/>
      <stop offset="0.35" stop-color="#8fae7a"/>
      <stop offset="0.6" stop-color="#5f8a3c"/>
      <stop offset="1" stop-color="#3f6a26"/>
    </linearGradient>
    <linearGradient id="verandah-table" x1="0" y1="0" x2="0" y2="1">
      <stop offset="0" stop-color="#a7b59a"/>
      <stop offset="0.35" stop-color="#8a7764"/>
      <stop offset="0.65" stop-color="#c99a5b"/>
      <stop offset="1" stop-color="#4a3d35"/>
    </linearGradient>
    <symbol id="icon-phone" viewBox="0 0 24 24"><path d="M6.6 3.5 9 6.2 7.7 8.4c.9 2.6 3 4.8 5.9 6l2.1-1.4 2.8 2.3-1.4 3.1C11 18.6 5.2 12.7 4.3 5z"/></symbol>
    <symbol id="icon-mobile" viewBox="0 0 24 24"><rect x="6.5" y="2.5" width="11" height="19" rx="2" fill="none" stroke-width="2"/><rect x="8.5" y="5" width="7" height="11" stroke="none"/></symbol>
    <symbol id="icon-mail" viewBox="0 0 24 24"><rect x="2.5" y="5.5" width="19" height="13" fill="none" stroke-width="2"/><path d="M3 6l9 7 9-7" fill="none" stroke-width="2"/></symbol>
    <symbol id="icon-social" viewBox="0 0 24 24"><rect x="3.5" y="3.5" width="17" height="17" rx="2" fill="none" stroke-width="2.4"/></symbol>
    <symbol id="icon-home" viewBox="0 0 24 24"><path d="M2 11 12 3l10 8h-3v9H5v-9z" stroke="none"/><rect x="10" y="14" width="4" height="6" fill="#fff" stroke="none"/></symbol>
  </defs>
</svg>

<main class="sheet">
  <h2 class="variant-label" style="left:105px;top:56px;">single</h2>

  <section class="card card--single">
    <svg class="card-art" width="972" height="597" viewBox="0 0 972 597">
      <path d="M0 0H300Q440 280 0 375Z" fill="url(#countryside)" role="img" aria-label="Photo of gum trees beside a green paddock and cane fields"/>
      <path d="M300 0Q440 280 0 375" fill="none" stroke="var(--arc-light)" stroke-width="4" transform="translate(6 6)"/>
      <path d="M300 0Q440 280 0 375" fill="none" stroke="var(--arc-blue)" stroke-width="9"/>
      <path d="M972 227H770Q640 380 745 597H972Z" fill="url(#verandah-table)" role="img" aria-label="Photo of a tomato galette and a bottle of olive oil on a verandah table"/>
      <path d="M770 227Q640 380 745 597" fill="none" stroke="var(--arc-light)" stroke-width="4" transform="translate(-7 0)"/>
      <path d="M770 227Q640 380 745 597" fill="none" stroke="var(--arc-blue)" stroke-width="9"/>
    </svg>
    <h1 class="brand-name">Larkhollow Pantry</h1>
    <ul class="services">
      <li>Gourmet market food</li>
      <li>Vintage Picnic Hampers</li>
      <li>Cooking Classes</li>
    </ul>
    <p class="tagline">Gourmet food made in my country kitchen, using fresh ingredients, for your enjoyment and convenience. Viv Harlow</p>
    <ul class="contacts" style="fill:var(--icon-navy);stroke:var(--icon-navy);">
      <li><svg><use href="#icon-phone"/></svg>0748216597</li>
      <li><svg><use href="#icon-mobile"/></svg>0412386951</li>
      <li><svg><use href="#icon-mail"/></svg>larkhollowpantry@postmail.net</li>
      <li><svg><use href="#icon-social"/></svg>Larkhollow Pantry</li>
      <li><svg><use href="#icon-home"/></svg>42 Tindale's Lane, Mt Orrin Via Brimsworth</li>
    </ul>
  </section>

  <h2 class="variant-label" style="left:125px;top:813px;">double-sided</h2>

  <section class="card card--front">
    <svg class="card-art" width="935" height="556" viewBox="0 0 935 556">
      <path d="M935 0H740Q560 300 707 556H935Z" fill="url(#verandah-table)" role="img" aria-label="Photo of a tomato galette and a bottle of olive oil on a verandah table"/>
      <path d="M740 0Q560 300 707 556" fill="none" stroke="var(--arc-light)" stroke-width="4" transform="translate(-8 0)"/>
      <path d="M740 0Q560 300 707 556" fill="none" stroke="var(--arc-blue)" stroke-width="9"/>
    </svg>
    <h1 class="brand-name">Larkhollow Pantry</h1>
    <ul class="services">
      <li>Gourmet market food</li>
      <li>Vintage Picnic Hampers</li>
      <li>Cooking Classes</li>
    </ul>
    <p class="tagline">Gourmet food made in my country kitchen, using fresh ingredients, for your enjoyment and convenience.<br>Viv Harlow</p>
  </section>

  <section class="card card--back">
    <svg class="card-art" width="941" height="557" viewBox="0 0 941 557">
      <path d="M0 0H211Q390 290 254 557H0Z" fill="url(#countryside)" role="img" aria-label="Photo of gum trees beside a green paddock and cane fields"/>
      <path d="M211 0Q390 290 254 557" fill="none" stroke="var(--arc-light)" stroke-width="4" transform="translate(8 0)"/>
      <path d="M211 0Q390 290 254 557" fill="none" stroke="var(--arc-blue)" stroke-width="9"/>
    </svg>
    <h1 class="brand-name">Larkhollow Pantry</h1>
    <ul class="contacts">
      <li><svg class="icon"><use href="#icon-phone"/></svg>0748216597</li>
      <li><svg class="icon"><use href="#icon-mobile"/></svg>0412386951</li>
      <li><svg class="icon"><use href="#icon-mail"/></svg>larkhollowpantry@postmail.net</li>
      <li><svg class="icon"><use href="#icon-social"/></svg>Larkhollow Pantry</li>
      <li><svg class="icon"><use href="#icon-home"/></svg>42 Tindale's Lane, Mt Orrin Via Brimsworth</li>
    </ul>
  </section>
</main>
</body>
</html>
```